Whimsical business cards and stationary for accessories and gifts company
Please use your design expertise!
Whimsical business cards and stationary for accessories and gifts company - Children
Creative Brief
Bright & Fun-filled
Marisa T Palvendo
Designer
Larkfield, Vermont
PipandLulaDesigns@brimletmail.com
www.PipAndLulaDesigns.craftvane.com www.friendloop.com/PipandLulaDesigns @PipAndLulaDesigns
Hair Accessories Party Favors Unique Gifts
Concepts
Business Cards for kids golf
Vanta Vanta
Kindly upload the Ai file of your logo.

```html
<!DOCTYPE html>
<html lang="en">
<head>
<meta charset="utf-8">
<title>Pip &amp; Lula Business Card</title>
<link href="https://fonts.googleapis.com/css2?family=Quicksand:wght@400;500;600&display=swap" rel="stylesheet">
<style>
  :root {
    --page-bg: #ecebea;
    --card-white: #ffffff;
    --card-shade: #e9e9e9;
    --brand-purple: #93298a;
    --text-grey: #555555;
    --text-light: #ffffff;
    --rule-grey: #9a9a9a;
  }
  html, body {
    margin: 0;
    width: 1200px;
    height: 904px;
    overflow: hidden;
    background: var(--page-bg);
    font-family: "Quicksand", sans-serif;
  }
  .stage {
    position: relative;
    width: 1200px;
    height: 904px;
  }
  .card {
    position: absolute;
    left: 250px;
    width: 700px;
    height: 400px;
    border-radius: 22px;
    overflow: hidden;
    box-shadow: 0 6px 18px rgba(0,0,0,0.18);
  }
  .card-front {
    top: 40px;
    background: linear-gradient(180deg, var(--card-white) 0%, var(--card-shade) 100%);
  }
  .front-mark {
    position: absolute;
    top: 110px;
    left: 0;
    right: 0;
    display: flex;
    align-items: center;
    justify-content: center;
    gap: 14px;
  }
  .mark-dot {
    width: 22px;
    height: 22px;
    border-radius: 50%;
    background: var(--brand-purple);
  }
  .brand-name {
    color: var(--brand-purple);
    font-weight: 600;
    font-size: 44px;
    letter-spacing: 1px;
  }
  .offerings {
    position: absolute;
    left: 40px;
    bottom: 58px;
    display: flex;
    align-items: center;
    color: var(--text-grey);
    font-size: 19px;
    font-weight: 500;
  }
  .offerings .divider {
    width: 1px;
    height: 20px;
    background: var(--rule-grey);
    margin: 0 16px;
  }
  .card-back {
    top: 464px;
    display: flex;
    background: var(--card-white);
  }
  .back-brand {
    width: 308px;
    display: flex;
    align-items: center;
    justify-content: center;
    gap: 10px;
    background: linear-gradient(180deg, var(--card-white) 0%, var(--card-shade) 100%);
  }
  .back-brand .brand-name { font-size: 38px; }
  .back-brand .mark-dot { width: 16px; height: 16px; }
  .back-details {
    flex: 1;
    background: var(--brand-purple);
    color: var(--text-light);
    padding: 40px 30px 0 34px;
  }
  .person-name {
    font-size: 24px;
    font-weight: 600;
    margin: 0;
  }
  .person-role {
    font-size: 16px;
    margin: 2px 0 18px;
  }
  .location {
    font-size: 16px;
    margin: 0 0 12px;
  }
  .contact-list {
    list-style: none;
    margin: 0;
    padding: 0;
    font-size: 15px;
  }
  .contact-list li {
    display: flex;
    align-items: center;
    gap: 12px;
    height: 27px;
    white-space: nowrap;
  }
  .contact-icon {
    width: 16px;
    height: 16px;
    flex: none;
  }
</style>
</head>
<body>
<main class="stage">
  <section class="card card-front">
    <div class="front-mark">
      <span class="mark-dot"></span>
      <span class="brand-name">pip &amp; lula</span>
    </div>
    <div class="offerings">
      <span>Hair Accessories</span>
      <span class="divider"></span>
      <span>Party Favors</span>
      <span class="divider"></span>
      <span>Unique Gifts</span>
    </div>
  </section>

  <section class="card card-back">
    <div class="back-brand">
      <span class="mark-dot"></span>
      <span class="brand-name">pip &amp; lula</span>
    </div>
    <div class="back-details">
      <p class="person-name">Marisa T Palvendo</p>
      <p class="person-role">Designer</p>
      <p class="location">Larkfield, Vermont</p>
      <ul class="contact-list">
        <li>
          <svg class="contact-icon" viewBox="0 0 16 16"><path d="M4 1.5h2.5l1 3.5-1.7 1.2a8 8 0 0 0 4 4L11 8.5l3.5 1V12c0 1.2-1 2-2 2A11 11 0 0 1 2 3.5c0-1 .8-2 2-2z" fill="#fff"/></svg>
          <span>(555) 014-2287</span>
        </li>
        <li>
          <svg class="contact-icon" viewBox="0 0 16 16"><rect x="1" y="3" width="14" height="10" rx="1" fill="#fff"/><path d="M1.5 3.5 8 9l6.5-5.5" stroke="#93298a" stroke-width="1.4" fill="none"/></svg>
          <span>PipandLulaDesigns@brimletmail.com</span>
        </li>
        <li>
          <svg class="contact-icon" viewBox="0 0 16 16"><circle cx="8" cy="8" r="6.5" stroke="#fff" stroke-width="1.4" fill="none"/><ellipse cx="8" cy="8" rx="3" ry="6.5" stroke="#fff" stroke-width="1.2" fill="none"/><path d="M1.5 8h13" stroke="#fff" stroke-width="1.2"/></svg>
          <span>www.PipAndLulaDesigns.craftvane.com</span>
        </li>
        <li>
          <svg class="contact-icon" viewBox="0 0 16 16"><circle cx="8" cy="8" r="6.5" fill="#fff"/></svg>
          <span>www.friendloop.com/PipandLulaDesigns</span>
        </li>
        <li>
          <svg class="contact-icon" viewBox="0 0 16 16"><circle cx="8" cy="8" r="6.5" fill="#fff"/></svg>
          <span>@PipAndLulaDesigns</span>
        </li>
      </ul>
    </div>
  </section>
</main>
</body>
</html>
```